Social Media Graphics - ALL TEXT RK

We are looking for a series of social media graphics for Instagram (standard size 1:1 (1080x1080px) that are ALL TEXT. We want the following quotes below on each graphic; one quote per graphic. AND, In very small letters at the bottom of each graphic, add @RKMarlowLive

The look and feel of these graphics should be complimentary to the color palette attached below; but keep them simple. But the design is up to you; at the end of this document, I provided various samples of all text graphics that I like as examples.

Target Market(s)

women looking to lose weight

Industry/Entity Type

health and wellness

Colors
E54698
E96AAD
F1A4CE
F9D9EA
FCEFF6

Requirements
Must have
• the quotes in the document
Should not have
• no stock photography

```html
<!DOCTYPE html>
<html lang="en">
<head>
<meta charset="utf-8">
<title>GLP-1 Quote Graphic</title>
<link href="https://fonts.googleapis.com/css2?family=Archivo+Black&family=Archivo:wght@800&display=swap" rel="stylesheet">
<style>
  :root {
    --bg-dark: #35141f;
    --bg-mid: #7a3055;
    --bg-light: #cf5292;
    --text-pale: #f8d7e8;
    --shadow-pink: #e0006a;
    --shadow-dark: #2e1420;
  }
  html, body {
    margin: 0;
    padding: 0;
    width: 1200px;
    height: 1200px;
    overflow: hidden;
  }
  .graphic {
    position: relative;
    width: 1200px;
    height: 1200px;
    background: linear-gradient(90deg, var(--bg-dark) 0%, var(--bg-mid) 45%, var(--bg-light) 100%);
  }
  .quote {
    position: absolute;
    left: 203px;
    top: 228px;
    margin: 0;
    width: 900px;
    font-family: "Archivo Black", "Arial Black", sans-serif;
    font-size: 70px;
    line-height: 90px;
    letter-spacing: -0.5px;
    text-transform: uppercase;
    color: var(--text-pale);
    text-shadow:
      -3px 3px 0 var(--shadow-pink),
      -6px 6px 0 var(--shadow-dark);
  }
  .handle {
    position: absolute;
    right: 128px;
    top: 880px;
    margin: 0;
    font-family: "Archivo", "Arial", sans-serif;
    font-weight: 800;
    font-size: 44px;
    letter-spacing: 0.5px;
    text-transform: uppercase;
    color: var(--text-pale);
    text-shadow:
      -2px 2px 0 var(--shadow-pink),
      -4px 4px 0 var(--shadow-dark);
  }
</style>
</head>
<body>
  <main class="graphic">
    <p class="quote">GLP-1: The magic<br>behind the weight<br>loss drugs. But<br>here’s the secret -<br>you can boost it<br>naturally without<br>a prescription!</p>
    <p class="handle">@RKMarlowLive</p>
  </main>
</body>
</html>
```